Vel Mark Lane
Racing Driver Coaching
Vel Mark Lane  - Automotive
Creative Brief
Automotive
www.velmarklane-example.com
The company offers racing driver coaching.
Data analysis and video review
Dislikes: Technical websites with waiting time for upload. Long intros. Likes: effective use of imagery, clear communication and sparing use of tech wizardry.
left side
http://www.derekfolwell-example.com/
http://www.gusterrill-example.com/
http://www.rorybranscott-example.com/driver_coaching.asp
Branscott's content is good, Gus's presentation is good.

```html
<!DOCTYPE html>
<html lang="en">
<head>
<meta charset="utf-8">
<title>Vel Mark Lane — Racing Driver Coaching</title>
<link href="https://fonts.googleapis.com/css2?family=Arimo:ital,wght@0,400;0,700;1,700&display=swap" rel="stylesheet">
<style>
  :root {
    --page: #0d0d0d;
    --panel: #161616;
    --red: #d8141b;
    --red-dark: #8f0b0f;
    --white: #ffffff;
    --text: #c9c9c9;
    --muted: #8a8a8a;
    --line: #3a3a3a;
  }
  * { box-sizing: border-box; margin: 0; padding: 0; }
  html, body { width: 1200px; height: 1018px; overflow: hidden; background: var(--page); }
  body { font-family: "Arimo", Arial, sans-serif; color: var(--text); position: relative; }

  .hero-photo {
    position: absolute; left: 0; top: 80px; width: 1200px; height: 460px;
    background:
      radial-gradient(ellipse at 68% 55%, #b3161c 0%, #6a0d10 28%, rgba(20,20,20,0) 60%),
      linear-gradient(180deg, #2a2a2a 0%, #1b1b1b 45%, #3a3633 80%, #121212 100%);
  }

  .brand { position: absolute; left: 150px; top: 26px; display: flex; align-items: center; gap: 10px; }
  .brand-mark { width: 16px; height: 16px; background: var(--red); }
  .brand-name { font-weight: 700; font-size: 40px; color: var(--white); letter-spacing: -0.5px; line-height: 1; }
  .brand-tag { position: absolute; left: 176px; top: 66px; font-size: 13px; color: var(--text); }

  .main-nav {
    position: absolute; left: 503px; top: 28px; width: 557px; height: 44px;
    background: #111; border-bottom: 4px solid var(--red); border-top: 2px solid var(--red-dark);
    display: flex; justify-content: space-around; align-items: center;
  }
  .main-nav a { color: var(--white); font-size: 13px; font-weight: 700; text-decoration: none; letter-spacing: 0.3px; }

  .hero-title {
    position: absolute; left: 151px; top: 150px; color: var(--white);
    font-size: 58px; line-height: 62px; font-weight: 400;
  }
  .cta {
    position: absolute; left: 157px; top: 358px; width: 262px; height: 68px;
    background: linear-gradient(180deg, #ee2a2f 0%, var(--red) 55%, #a80f14 100%);
    color: var(--white); font-size: 30px; display: flex; align-items: center; justify-content: center;
    border-radius: 3px;
  }

  .feature { position: absolute; top: 550px; width: 270px; }
  .feature-photo { height: 138px; }
  .feature-label {
    height: 32px; background: linear-gradient(180deg, #e01a20, var(--red-dark));
    color: var(--white); font-size: 14px; padding: 8px 12px;
  }
  .feature-body { padding: 16px 0 0 0; font-size: 12px; line-height: 16px; height: 130px; }
  .feature-body ul { list-style: none; }
  .feature-body li::before { content: "» "; color: var(--red); }
  .news-date { color: var(--red); }
  .news-link { color: var(--white); text-decoration: underline; margin-bottom: 6px; display: block; }
  .read-more {
    display: inline-block; margin-top: 8px; width: 95px; height: 20px;
    background: var(--red); color: var(--white); font-size: 10px; padding: 4px 8px;
  }

  .site-footer { position: absolute; top: 895px; left: 0; width: 1200px; height: 123px; }
  .footer-col { position: absolute; top: 0; font-size: 12px; line-height: 17px; }
  .footer-col h4 {
    font-style: italic; font-weight: 700; color: var(--white); font-size: 12px;
    text-decoration: underline; margin-bottom: 10px;
  }
  .footer-brand { position: absolute; left: 784px; top: 0; }
  .footer-brand .name { font-weight: 700; font-size: 34px; color: #9a9a9a; line-height: 1; }
  .footer-brand .tag { font-size: 12px; color: var(--muted); margin: 4px 0 6px 2px; }
  .footer-brand .legal { font-size: 11px; line-height: 14px; }
</style>
</head>
<body>
  <div class="hero-photo" role="img" aria-label="Red single-seater racing car with driver in helmet, speeding across a blurred track"></div>

  <header>
    <div class="brand"><span class="brand-mark"></span><span class="brand-name">Vel Mark Lane</span></div>
    <div class="brand-tag">Racing Driver Coaching</div>
    <nav class="main-nav">
      <a href="#">HOME</a><a href="#">ABOUT US</a><a href="#">SERVICES</a><a href="#">GALLERY</a><a href="#">NEWS</a><a href="#">PARTNERS</a><a href="#">CONTACT US</a>
    </nav>
  </header>

  <h1 class="hero-title">Be The Part of<br>Winning<br>Combination</h1>
  <a class="cta">JOIN US NOW!</a>

  <section class="feature" style="left:160px">
    <div class="feature-photo" role="img" aria-label="Two racing drivers in red suits celebrating on the podium" style="background:linear-gradient(135deg,#3a6fb0,#b51a1f 60%,#6d0c10)"></div>
    <div class="feature-label">About Vel Mark Lane</div>
    <div class="feature-body">Harcourt Wealth is committed to meeting the needs of wealthy clients and those aspiring to become wealthier. We understand that wealth is more than money.</div>
    <a class="read-more">Read More »</a>
  </section>

  <section class="feature" style="left:462px">
    <div class="feature-photo" role="img" aria-label="Red racing car on track, front three-quarter view" style="background:linear-gradient(160deg,#2b2b2b,#9d1419 55%,#3b3b3b)"></div>
    <div class="feature-label">Coaching &amp; Training</div>
    <div class="feature-body"><ul>
      <li>Mauris auctor elementum quam</li>
      <li>Ut nunc eros, sodales eget semper in</li>
      <li>Feugiat quis nunc diam venenatis</li>
      <li>Ipsum non mi feugiat consequat</li>
    </ul></div>
    <a class="read-more">Read More »</a>
  </section>

  <section class="feature" style="left:770px">
    <div class="feature-photo" role="img" aria-label="Grid of racing cars on a green-edged circuit at race start" style="background:linear-gradient(180deg,#cfd6dc,#7e9a5a 45%,#5d5d5d 75%,#3e3e3e)"></div>
    <div class="feature-label">News &amp; Events</div>
    <div class="feature-body">
      <span class="news-date">» 17 March 2011, London</span>
      <span class="news-link">Harcourt Wealth Appoints New Head of Fiduciary</span>
      <span class="news-date">» 19 February 2011, London</span>
      <span class="news-link">Harcourt Wealth wins six Meridian Finance</span>
    </div>
    <a class="read-more">Read More »</a>
  </section>

  <footer class="site-footer">
    <div class="footer-col" style="left:160px">
      <h4>Vel Mark Lane</h4>
      Corporate Entertainment<br>Brand Promotion<br>About Us<br>Driver Coaching
    </div>
    <div class="footer-col" style="left:371px">
      <h4>Community</h4>
      News<br>Blog<br>Tips<br>Forum
    </div>
    <div class="footer-col" style="left:523px">
      <h4>Quick Contact</h4>
      Mobile: +44 (0)7700 900123<br>Office: +44 (0)191 4960321<br>Email: coach@velmarklane-example.com<br>Web: www.velmarklane-example.com
    </div>
    <div class="footer-brand">
      <div class="name">Vel Mark Lane</div>
      <div class="tag">Racing Driver Coaching</div>
      <div class="legal">© Copyrights 2011 velmarklane-example.com<br>All Rights Reserved</div>
    </div>
  </footer>
</body>
</html>
```